Accountancy firm needs clean and simple website and optional logo

We need a logo and basic wordpress website design for a Sydney based accountancy firm.
We need a clean and simple logo and website, based on the accounting/finance/tax industry. Simple, credible and official colors.
The logo is expected to be so simple that we have combined into the one job.
If you submit a logo design and we choose it along with someone else's website design you will be paid a bonus of $60. The website design will still win the competition as per normal.
Current website is old and terrible but gives you an idea of the sitemap (super simple) and what they do: www.brookfiscal.com.au
We want original different to normal template looking designs.
We like videos, and like http://www.whitfords.com.au/
Feel free to go to vidhaven and use some videos from there.
We are based in Sydney Australia and in the field of taxation and accounting
We want a clean, formal, credible site, limited pages.
The project is guaranteed, so go for it.
Brook & Associates
1 page

```html
<!DOCTYPE html>
<html lang="en">
<head>
<meta charset="utf-8">
<title>Brook &amp; Associates – Tax Accountants</title>
<link rel="stylesheet" href="https://fonts.googleapis.com/css2?family=Arvo&family=Roboto:wght@400;500&display=swap">
<style>
  :root {
    --brand-blue: #069ff5;
    --ring-white: #ffffff;
    --panel-dark: #222222;
    --sky-top: #2f3c48;
    --sky-mid: #3c4753;
    --sand: #6b5e4f;
    --text-light: #ffffff;
  }
  * { margin: 0; padding: 0; box-sizing: border-box; }
  html, body { width: 975px; height: 1200px; overflow: hidden; }
  body { font-family: "Arvo", Georgia, serif; color: var(--text-light); }
  .page { position: relative; width: 975px; height: 1200px; overflow: hidden; }

  .backdrop {
    position: absolute; inset: 0;
    background: linear-gradient(180deg, var(--sky-top) 0%, var(--sky-mid) 55%, #4b5257 72%, var(--sand) 90%, #5e5246 100%);
  }

  .disc {
    position: absolute; border-radius: 50%;
    background: var(--ring-white);
    box-shadow: 0 0 18px rgba(255,255,255,0.35);
  }
  .disc .core { position: absolute; border-radius: 50%; background: var(--brand-blue); }
  .disc.dark .core { background: var(--panel-dark); }

  .masthead { left: 242px; top: -284px; width: 488px; height: 488px; }
  .masthead .core { left: 28px; top: 28px; width: 432px; height: 432px; }
  .footer-disc { left: 238px; top: 994px; width: 496px; height: 496px; }
  .footer-disc .core { left: 32px; top: 32px; width: 432px; height: 432px; }

  .brand-name {
    position: absolute; left: 0; width: 975px; top: 58px; text-align: center;
    font-family: "Arvo", Georgia, serif; font-weight: 400; font-size: 22px; line-height: 26px;
  }

  .nav-disc { width: 204px; height: 204px; }
  .nav-disc .core { left: 14px; top: 14px; width: 176px; height: 176px; display: flex; flex-direction: column; align-items: center; justify-content: center; gap: 6px; }
  .nav-label { font-size: 21px; }
  .nav-home { left: 45px; top: 84px; }
  .nav-about { left: 730px; top: 84px; }
  .nav-testimonials { left: 45px; top: 892px; }
  .nav-contact { left: 730px; top: 892px; }
  .nav-testimonials .nav-label, .nav-contact .nav-label { font-size: 19px; }

  .side-left { left: -300px; top: 332px; width: 504px; height: 504px; }
  .side-left .core { left: 24px; top: 24px; width: 456px; height: 456px; }
  .side-right { left: 770px; top: 330px; width: 508px; height: 508px; }
  .side-right .core { left: 24px; top: 24px; width: 460px; height: 460px; }

  .social { position: absolute; width: 37px; height: 36px; border: 1px solid rgba(255,255,255,0.8); }
  .social.active { background: var(--ring-white); border: none; }

  .call-us {
    position: absolute; left: 806px; top: 560px; width: 160px; text-align: center;
    font-family: "Roboto", Arial, sans-serif; font-size: 17px; line-height: 22px;
  }

  .service {
    position: absolute; border: 12px solid var(--ring-white); background: var(--panel-dark);
    box-shadow: 0 0 14px rgba(255,255,255,0.3);
  }
  .service-tax { left: 234px; top: 333px; width: 241px; height: 241px; border-radius: 0 50% 50% 50%; transform: rotate(-2deg); }
  .service-gst { left: 499px; top: 333px; width: 242px; height: 241px; border-radius: 50% 0 50% 50%; transform: rotate(2deg); }
  .service-litigation { left: 364px; top: 598px; width: 218px; height: 218px; border-radius: 50% 50% 50% 0; transform: rotate(-32deg); }

  .service-label {
    position: absolute; width: 200px; text-align: center; font-size: 14.5px; line-height: 19px;
    display: flex; flex-direction: column; align-items: center;
  }
  .label-tax { left: 248px; top: 415px; gap: 24px; }
  .label-gst { left: 523px; top: 417px; gap: 24px; }
  .label-litigation { left: 372px; top: 671px; gap: 30px; }

  .copyright {
    position: absolute; left: 0; width: 975px; top: 1124px; text-align: center;
    font-family: "Roboto", Arial, sans-serif; font-size: 9.5px;
  }
</style>
</head>
<body>
<main class="page">
  <div class="backdrop" role="img" aria-label="Dim beach scene with a thatched umbrella and two deck chairs"></div>

  <header class="disc masthead"><div class="core"></div></header>
  <p class="brand-name">BROOK &amp; ASSOCIATES</p>

  <nav>
    <a class="disc nav-disc nav-home"><span class="core">
      <svg width="34" height="30" viewBox="0 0 34 30"><path d="M17 2 L2 15 H7 V28 H14 V20 H20 V28 H27 V15 H32 Z" fill="#fff"/></svg>
      <span class="nav-label">HOME</span></span></a>
    <a class="disc nav-disc nav-about"><span class="core">
      <svg width="38" height="38" viewBox="0 0 38 38"><circle cx="19" cy="19" r="15" fill="none" stroke="#fff" stroke-width="6"/><circle cx="19" cy="19" r="15" fill="none" stroke="#069ff5" stroke-width="6" stroke-dasharray="6 17.5" stroke-dashoffset="3"/></svg>
      <span class="nav-label">ABOUT US</span></span></a>
    <a class="disc nav-disc nav-testimonials"><span class="core">
      <svg width="38" height="30" viewBox="0 0 38 30"><rect x="1" y="1" width="36" height="28" rx="4" fill="#fff"/><path d="M2 4 L19 17 L36 4" fill="none" stroke="#069ff5" stroke-width="2.5"/></svg>
      <span class="nav-label">TESTIMONIALS</span></span></a>
    <a class="disc nav-disc nav-contact"><span class="core">
      <svg width="24" height="34" viewBox="0 0 24 34"><path d="M12 1 C5 1 1 6 1 12 C1 20 12 33 12 33 C12 33 23 20 23 12 C23 6 19 1 12 1 Z" fill="#fff"/><circle cx="12" cy="12" r="4.5" fill="#069ff5"/></svg>
      <span class="nav-label">CONTACT US</span></span></a>
  </nav>

  <aside class="disc dark side-left"><div class="core"></div></aside>
  <span class="social" style="left:44px;top:490px" aria-label="Video channel"></span>
  <span class="social" style="left:44px;top:547px" aria-label="Professional network"></span>
  <span class="social" style="left:44px;top:605px" aria-label="Microblog"></span>
  <span class="social" style="left:44px;top:662px" aria-label="Photo sharing"></span>
  <span class="social active" style="left:100px;top:572px" aria-label="Social page"></span>

  <aside class="disc dark side-right"><div class="core"></div></aside>
  <p class="call-us">Call Us<br>02 9000 4172</p>

  <section>
    <div class="service service-tax"></div>
    <div class="service service-gst"></div>
    <div class="service service-litigation"></div>

    <div class="service-label label-tax">
      <svg width="30" height="30" viewBox="0 0 30 30"><rect x="5" y="2" width="20" height="26" rx="2" fill="#069ff5"/><path d="M9 9 H21 M9 14 H21 M9 19 H17" stroke="#222" stroke-width="2"/></svg>
      <span>TAX PLANNING<br>AND RETURNS</span>
    </div>
    <div class="service-label label-gst">
      <svg width="32" height="32" viewBox="0 0 32 32"><circle cx="16" cy="16" r="13" fill="none" stroke="#069ff5" stroke-width="3.5"/><path d="M16 9 V17 H11" fill="none" stroke="#069ff5" stroke-width="3"/></svg>
      <span>GST PREPARATION<br>AND LODGEMENT</span>
    </div>
    <div class="service-label label-litigation">
      <svg width="42" height="38" viewBox="0 0 42 38"><circle cx="15" cy="21" r="10" fill="none" stroke="#069ff5" stroke-width="6" stroke-dasharray="4 3"/><circle cx="15" cy="21" r="5" fill="#069ff5"/><circle cx="32" cy="9" r="6" fill="none" stroke="#069ff5" stroke-width="4" stroke-dasharray="3 2"/><circle cx="32" cy="30" r="5" fill="none" stroke="#069ff5" stroke-width="4" stroke-dasharray="3 2"/></svg>
      <span>LITIGATION<br>ASSISTANCE</span>
    </div>
  </section>

  <footer class="disc footer-disc"><div class="core"></div></footer>
  <p class="copyright">Copyright 2015 Comapny Name. All Rights Reserved.</p>
</main>
</body>
</html>
```